Veltrano - Mechanic/Collision Center Business Card

We're looking for a business card design for our mechanic/ collision repair shop.

Can be with colours or monochromatic.

See the attached files.

Many thanks

```html
<!DOCTYPE html>
<html lang="en">
<head>
<meta charset="utf-8">
<title>Veltrano Business Card</title>
<link href="https://fonts.googleapis.com/css2?family=Mulish:wght@400;600;800;900&display=swap" rel="stylesheet">
<style>
  :root {
    --page-bg: #e6eaee;
    --brand-navy: #2b6189;
    --brand-blue: #3a88cc;
    --ink: #1e1f22;
    --ink-soft: #444a50;
    --card-white: #ffffff;
    --shadow: rgba(20, 40, 60, 0.18);
  }
  * { margin: 0; padding: 0; box-sizing: border-box; }
  html, body { width: 1200px; height: 1200px; overflow: hidden; }
  body {
    background: var(--page-bg);
    font-family: "Mulish", "Century Gothic", sans-serif;
    color: var(--ink);
    display: flex;
    flex-direction: column;
    align-items: center;
    justify-content: center;
    gap: 60px;
  }
  .card {
    position: relative;
    width: 880px;
    height: 500px;
    overflow: hidden;
    box-shadow: 0 10px 30px var(--shadow);
  }
  .card__stripe {
    position: absolute;
    left: 0; right: 0; bottom: 0;
    height: 22px;
    background: var(--brand-blue);
  }

  /* front */
  .card--front { background: var(--card-white); }
  .front__brand {
    position: absolute;
    left: 40px; top: 150px;
    width: 340px;
    text-align: center;
  }
  .brand-name {
    font-weight: 900;
    font-size: 62px;
    letter-spacing: 1px;
    text-transform: uppercase;
    color: var(--ink);
    line-height: 1;
  }
  .brand-dot {
    display: inline-block;
    width: 18px; height: 18px;
    border-radius: 50%;
    background: var(--brand-blue);
    margin-bottom: 14px;
  }
  .brand-est {
    margin-top: 12px;
    font-weight: 800;
    font-size: 16px;
    letter-spacing: 3px;
    color: var(--ink);
  }
  .front__divider {
    position: absolute;
    left: 405px; top: 70px;
    width: 4px; height: 330px;
    background: var(--brand-blue);
    transform: skewX(-14deg);
    transform-origin: bottom;
  }
  .front__details {
    position: absolute;
    left: 530px; top: 110px;
  }
  .person__name {
    font-weight: 800;
    font-size: 38px;
    letter-spacing: 1px;
    text-transform: uppercase;
    line-height: 1;
  }
  .person__role {
    font-weight: 800;
    font-size: 18px;
    color: var(--brand-blue);
    text-transform: uppercase;
    letter-spacing: 1px;
    margin-top: 4px;
  }
  .contact-list { list-style: none; margin-top: 26px; }
  .contact-list li {
    display: flex;
    align-items: flex-start;
    gap: 14px;
    font-size: 17px;
    line-height: 1.45;
    color: var(--ink-soft);
    margin-bottom: 8px;
  }
  .contact-list svg { flex: 0 0 18px; width: 18px; height: 18px; margin-top: 3px; fill: var(--brand-blue); }

  /* back */
  .card--back { background: var(--brand-navy); color: var(--card-white); }
  .back__brand {
    position: absolute;
    left: 0; right: 0; top: 150px;
    text-align: center;
  }
  .card--back .brand-name { color: var(--card-white); font-size: 84px; }
  .card--back .brand-dot { background: var(--card-white); }
  .card--back .brand-est { color: var(--card-white); }
  .back__web {
    position: absolute;
    left: 0; right: 0; bottom: 44px;
    display: flex; justify-content: center; align-items: center; gap: 10px;
    font-weight: 600;
    font-size: 20px;
    letter-spacing: 0.5px;
  }
  .web-square { width: 16px; height: 16px; background: var(--card-white); }
</style>
</head>
<body>

  <section class="card card--front">
    <div class="front__brand">
      <span class="brand-dot"></span>
      <div class="brand-name">Veltrano</div>
      <div class="brand-est">EST. 1979</div>
    </div>

    <div class="front__divider"></div>

    <div class="front__details">
      <div class="person__name">Rui Matos</div>
      <div class="person__role">Manager</div>
      <ul class="contact-list">
        <li>
          <svg viewBox="0 0 24 24"><path d="M12 3 2 12h3v9h5v-6h4v6h5v-9h3z"/></svg>
          <span>Rua das Oficinas, 42<br>1900-118 Lisboa</span>
        </li>
        <li>
          <svg viewBox="0 0 24 24"><path d="M6.6 10.8a15 15 0 0 0 6.6 6.6l2.2-2.2c.3-.3.7-.4 1-.2 1.1.4 2.3.6 3.6.6.6 0 1 .4 1 1V20c0 .6-.4 1-1 1A17 17 0 0 1 3 4c0-.6.4-1 1-1h3.5c.6 0 1 .4 1 1 0 1.3.2 2.5.6 3.6.1.3 0 .7-.2 1z"/></svg>
          <span>+351 214557302<br>+351 913480266</span>
        </li>
        <li>
          <svg viewBox="0 0 24 24"><path d="M2 5h20v14H2zm2 2v.5l8 5 8-5V7z"/></svg>
          <span>veltrano.oficina@mail.com</span>
        </li>
        <li>
          <svg viewBox="0 0 24 24"><rect x="3" y="3" width="18" height="18" rx="2"/></svg>
          <span>www.veltrano-auto.pt</span>
        </li>
      </ul>
    </div>

    <div class="card__stripe"></div>
  </section>

  <section class="card card--back">
    <div class="back__brand">
      <span class="brand-dot"></span>
      <div class="brand-name">Veltrano</div>
      <div class="brand-est">EST. 1979</div>
    </div>
    <div class="back__web">
      <span class="web-square"></span>
      <span>www.veltrano-auto.pt</span>
    </div>
    <div class="card__stripe"></div>
  </section>

</body>
</html>
```